Brookwell Fields tea

We are relaunching our new bottle of Guayusa energy tea.
Guayusa is cultivate carefully by The native South American Amazonian farmers, with a diverse mix of food crops, herbs, hardwood trees, fruit trees, spices, medicinal plants and the Guayusa Trees. The farming process that takes place in harmony with the Amazon Rainforest and the diversity of their gardens reflects this attitude toward the natural world.

The company was establish in 2014 and goes by until the pandemic. When all the operations stoped. Now we want to enter again into the USA market with many improvements in the bottle image, we want to use glass bottle so the costumer can look into the color of the tea but with a logo that stand ups, nutritional information and benefits for your health with the Guayusa energy tea
like:
Acecelerate Metabolism
24 Vitamins and Minerals
Burns Calories & Body fat
Provide essential energy

Brewed From Guayusa : used throughout centuries for its healing properties, focused mental clarity, and potent health effects!

Sweetened With Natural Agave :healthy alternative to sugar & artificial sweeteners with a more smooth, flavorful taste than other teas!

Sooth & Stimulating : abundance of caffeine that is slowly released to provide a smooth and pleasant stimulus for waking up in the morning!

Low Glycemic Index :stabilizes blood sugar levels to promote weight loss, boost cardiovascular health & prevent type 2 diabetes!

2 x As Many Antioxidants as Green tea : great for immune system health, eliminating free radicals & fighting/preventing cancer!

Excellent Source of Nutrition — provides an array of 11 polyphenols, 15 amino acids & 24 vitamins and minerals for healthy, balanced diet!

Target Market(s)

eeuu

Industry/Entity Type

beverages industry

Colors
FFC000
F8CF3A
FAE287
FDF2CF
FEFAEE

Requirements
Must have
• Glass bottle designs, full label

```html
<!DOCTYPE html>
<html lang="en">
<head>
<meta charset="utf-8">
<title>Guayusa Energy Tea – Bottle Label</title>
<link rel="stylesheet" href="https://fonts.googleapis.com/css2?family=Oswald:wght@500&family=Roboto:wght@900&family=Montserrat:wght@500&display=swap">
<style>
  :root {
    --stage: #555656;
    --label-dark: #1b1e1c;
    --leaf-lime: #9cc42a;
    --leaf-green: #3f9a4a;
    --leaf-deep: #1f6b3a;
    --text-light: #f2f2f2;
    --tag-grey: #5d6061;
  }
  * { margin: 0; padding: 0; box-sizing: border-box; }
  html, body { width: 1200px; height: 1197px; overflow: hidden; }
  body { background: var(--stage); position: relative; }

  .neck-tag {
    position: absolute; left: 200px; top: 100px;
    width: 64px; height: 300px; background: var(--tag-grey);
    display: flex; align-items: center; justify-content: center;
  }
  .neck-tag__name {
    transform: rotate(90deg);
    font-family: "Montserrat", sans-serif; font-weight: 500;
    font-size: 34px; color: var(--text-light); white-space: nowrap;
  }

  .label {
    position: absolute; left: 425px; top: 100px;
    width: 650px; height: 1000px; background: var(--label-dark);
  }
  .label__product {
    position: absolute; left: 0; right: 0; top: 70px;
    text-align: center;
    font-family: "Montserrat", sans-serif; font-weight: 500;
    font-size: 100px; line-height: 1;
    color: var(--text-light);
  }
  .label__type {
    position: absolute; left: 82px; top: 635px;
    transform: rotate(-90deg); transform-origin: left top;
    font-family: "Roboto", sans-serif; font-weight: 900;
    font-size: 64px; line-height: 1; white-space: nowrap;
    color: var(--text-light);
  }
  .label__type-accent { color: var(--leaf-lime); }
  .benefits {
    position: absolute; left: 210px; top: 262px;
    list-style: none;
    font-family: "Montserrat", sans-serif; font-weight: 500;
    font-size: 25px; line-height: 45px; color: var(--text-light);
  }
  .benefits li::before { content: "•"; margin-right: 14px; }
  .benefits__accent { color: var(--leaf-lime); }
  .label__sweetener {
    position: absolute; left: 190px; width: 350px; top: 535px;
    text-align: center;
    font-family: "Oswald", sans-serif; font-weight: 500;
    font-size: 40px; line-height: 1.2; color: var(--text-light);
  }
  .label__foliage {
    position: absolute; left: 0; right: 0; bottom: 0; height: 333px;
    background: linear-gradient(120deg, var(--leaf-lime) 0%, var(--leaf-green) 45%, var(--leaf-deep) 70%, var(--leaf-lime) 100%);
  }
</style>
</head>
<body>
  <div class="neck-tag">
    <span class="neck-tag__name">Guayusa</span>
  </div>

  <section class="label">
    <h1 class="label__product">Guayusa</h1>
    <p class="label__type">energy <span class="label__type-accent">tea</span></p>
    <ul class="benefits">
      <li>Acecelerate <span class="benefits__accent">Metabolism</span></li>
      <li>24 <span class="benefits__accent">Vitamins and Minerals</span></li>
      <li>Burns <span class="benefits__accent">Calories &amp; Body fat</span></li>
      <li>Provide <span class="benefits__accent">essential energy</span></li>
    </ul>
    <p class="label__sweetener">Sweetened With<br>Natural Agave</p>
    <div class="label__foliage" role="img" aria-label="Tropical monstera leaf pattern in lime and green tones"></div>
  </section>
</body>
</html>
```